120ml Jar Label — Masculine Cosmetic Foot Balm for Cracked, Hardworking Heels

We need a print-ready wraparound label for a 120ml jar — a brown/amber glass jar with a black metal screw lid (file photo attached).

--DO NOT PUT A BARCODE ON THE LABEL PLEASE--
**PLEASE READ "PLAN HUDDLE PROJECT BRIEF FINAL.MD" IN ATTACHED FILES IF YOU ARE SUBMITTING A DESIGN.**

The label is 190mm wide × 40mm high.
We need files to be in an .ai format with a 2mm bleed at the end.
Social media handle: @bramblekeepnz (facebook, instagram and tiktok)

Bramble Keep is a New Zealand foot-care brand making practical, no-nonsense products for hardworking men whose jobs wreck their feet. Our flagship product, Ridge Mender Balm, helps fix thick, cracked, hardworking skin.

Brand color scheme and overview is all in the brief file. You may add some brand aligned colors outside of the specified hex codes as you see fit to make a great design. Feel free to remove the "Bramble Keep" text from the logo so Bramble Keep is not doubled up on the front of the label

The tone we want: direct, rugged, and credible — like a workwear brand, not a spa brand. Most cracked-heel products on the market lean soft and feminine; we want to stand apart by looking like a serious fix for a real problem, made in New Zealand.

Full legal requirements for New Zealand cosmetic labelling (ingredients, directions, net contents, origin, etc.) are listed in the attached brief document — these are non-negotiable and must stay legible.

Please see the label attached "Label spacing guide" for this project's rough spacing guide. This label is the same size and sits well on the jar. This label doesn't need to be spaced quite as much as the Verin Label

I want to run the design for a week - I feel 7 days is a good amount of time for designers to see the work, digest the brief and create something remarkable and memorable for Bramble Keep.

Target Market(s)

Working men in New Zealand whose jobs or lifestyle put heavy wear on their feet — tradies, farmers, hospital/shift workers, hunters, and outdoors people. Practical, value-driven buyers rather than luxury skincare shoppers.

Industry/Entity Type

Beauty / Health & Wellness / Cosmetics

Font styles to use
Sans Serif
Other font styles liked:
• Montserrat (bold, headings), Inter (regular, body)

Colors
00AB8E
00BBA5
67D7C9
C6EFE9
E9F9F6
FFC000
F8CF3A
FAE287
FDF2CF
FEFAEE

Requirements
Must have
• All NZ cosmetic labelling requirements from the attached brief (product name, tag line, net contents, ingredients, directions, storage, made in NZ) — legible and complete, not omitted for aesthetics Fits 190mm × 40mm wraparound format for a 120ml brown jar with black lid Uses our existing brand colors: Deep Olive #3C4A34, Bone White #F4EFE6, Terracotta Clay #C1683D, and Warm Grey #4A4540 (exact palette in attached brief) Uses Montserrat (headings) and Inter (body) or close equivalents Incorporates our existing shield-and-wing logo (attached) Brand name and product name clearly readable from a normal shelf/bathroom-cabinet distance
Nice to have
• A style that could extend into a hero/product photo later, similar to the NZ-hills-backdrop look on our website (screenshot attached) — not required for the label itself, just good to keep in mind Original icon work (e.g. a small soak/apply/sock icon set) if it fits the rugged brand feel A design that could work as a small back-label/wraparound split if the front can't fit everything at a readable size
Should not have
• No pastel colors, floral motifs, or delicate script fonts — this should never look like spa/luxury skincare. Don't introduce new brand colors outside the palette provided other than black.

```html
<!DOCTYPE html>
<html lang="en">
<head>
<meta charset="utf-8">
<title>Bramble Keep — Ridge Mender Balm Jar Label</title>
<link href="https://fonts.googleapis.com/css2?family=Inter:wght@400;600;700&family=Montserrat:wght@700;800&display=swap" rel="stylesheet">
<style>
  :root {
    --backdrop: #9d9ca7;
    --frame-brown: #8a5a2b;
    --bone: #f4efe6;
    --slate: #33404c;
    --heading-brown: #8b5523;
    --ink: #3a3532;
    --title-cream: #f3e2c4;
    --terracotta: #c1683d;
    --badge-green: #1f3a2b;
    --rule: #9a6a3a;
    --icon-ink: #5a4a3e;
  }
  * { box-sizing: border-box; margin: 0; padding: 0; }
  html, body { width: 1200px; height: 533px; overflow: hidden; }
  body {
    background: var(--backdrop);
    position: relative;
    font-family: "Inter", Arial, sans-serif;
    color: var(--ink);
  }
  .variant-number {
    position: absolute;
    left: 72px;
    width: 44px;
    text-align: center;
    font-size: 54px;
    font-weight: 400;
    color: #111;
    line-height: 1;
  }
  .label {
    position: absolute;
    left: 147px;
    width: 967px;
    height: 204px;
    background: var(--frame-brown);
    border-radius: 15px;
    padding: 8px;
  }
  .label-inner {
    position: relative;
    width: 951px;
    height: 188px;
    background: var(--bone);
    border-radius: 10px;
    overflow: hidden;
  }
  /* Left panel */
  .storage, .ingredients {
    position: absolute;
    left: 19px;
    width: 240px;
    font-size: 11.2px;
    line-height: 12.4px;
  }
  .storage { top: 19px; }
  .ingredients { top: 65px; }
  .field-title { color: var(--heading-brown); font-weight: 700; }
  .divider {
    position: absolute;
    left: 20px; top: 56px;
    width: 239px; height: 1px;
    background: var(--rule);
  }
  .tagline {
    position: absolute;
    left: 18px; top: 149px;
    font-size: 11px;
    line-height: 12.6px;
    text-transform: uppercase;
  }
  .tagline strong { color: var(--heading-brown); font-weight: 700; display: block; }
  .social-handle {
    position: absolute;
    left: 170px; top: 156px;
    font-size: 10.6px;
    display: flex; align-items: center; gap: 5px;
  }
  .social-dot { width: 8px; height: 8px; border-radius: 50%; background: var(--ink); }
  /* Front panel */
  .front {
    position: absolute;
    left: 283px; top: 0;
    width: 386px; height: 188px;
    background: var(--slate);
  }
  .fern-area { position: absolute; inset: 0; }
  .fern-area.dark {
    background: linear-gradient(90deg, rgba(30,39,48,0.8) 0%, rgba(30,39,48,0) 22%, rgba(30,39,48,0) 78%, rgba(30,39,48,0.8) 100%);
  }
  .fern-area.light {
    background: linear-gradient(90deg, rgba(72,90,110,0.6) 0%, rgba(72,90,110,0) 22%, rgba(72,90,110,0) 78%, rgba(72,90,110,0.6) 100%);
  }
  .brand {
    position: absolute;
    left: 0; right: 0; top: 9px;
    display: flex; align-items: center; justify-content: center; gap: 10px;
  }
  .brand-mark { width: 36px; height: 36px; border-radius: 50%; background: var(--terracotta); }
  .brand-name {
    font-family: "Montserrat", Arial, sans-serif;
    font-weight: 700;
    color: var(--title-cream);
    font-size: 19px;
    line-height: 1;
  }
  .product-name {
    position: absolute;
    left: 0; right: 0; top: 70px;
    text-align: center;
    font-family: "Montserrat", Arial, sans-serif;
    font-weight: 800;
    color: var(--title-cream);
    font-size: 32px;
    line-height: 32px;
    text-transform: uppercase;
  }
  .product-tagline {
    position: absolute;
    left: 115px; top: 139px;
    width: 154px; height: 17px;
    border-radius: 9px;
    background: var(--terracotta);
    color: var(--title-cream);
    font-size: 11.5px;
    line-height: 17px;
    text-align: center;
    letter-spacing: 0.3px;
  }
  .net-contents {
    position: absolute;
    left: 74px; top: 166px;
    color: var(--title-cream);
    font-size: 9px;
    letter-spacing: 0.6px;
  }
  .origin-badge {
    position: absolute;
    left: 282px; top: 156px;
    width: 68px; height: 24px;
    background: var(--badge-green);
    border: 1.5px solid var(--title-cream);
    color: var(--title-cream);
    text-align: center;
    font-family: "Montserrat", Arial, sans-serif;
  }
  .origin-badge b { display: block; font-size: 11px; line-height: 13px; font-weight: 800; }
  .origin-badge small { display: block; font-size: 5.6px; line-height: 7px; letter-spacing: 1.3px; font-weight: 700; border-top: 1px solid var(--title-cream); }
  /* Directions panel */
  .directions { position: absolute; left: 669px; top: 0; width: 282px; height: 188px; }
  .directions-title {
    position: absolute; left: 0; right: 0; top: 6px;
    text-align: center;
    color: var(--heading-brown);
    font-weight: 700; font-size: 13px;
  }
  .step-icon { position: absolute; left: 24px; width: 36px; height: 36px; }
  .step-text {
    position: absolute; left: 72px; width: 200px;
    font-size: 11.2px; line-height: 12.4px;
  }
  .icon-placeholder { border-radius: 8px; background: var(--icon-ink); }
  .icon-placeholder.foot { left: 28px; width: 28px; opacity: 0.25; }
  .icon-placeholder.sock { left: 27px; width: 30px; background: var(--frame-brown); }
  .pao-icon { position: absolute; left: 240px; top: 148px; width: 30px; height: 32px; }
</style>
</head>
<body>

<div class="variant-number" style="top:121px;">1</div>
<div class="variant-number" style="top:359px;">2</div>

<section class="label" style="top:45px;">
  <div class="label-inner">
    <p class="storage"><span class="field-title">STORAGE:</span> Keep out of direct sunlight. Best used within six months of opening.</p>
    <div class="divider"></div>
    <p class="ingredients"><span class="field-title">INGREDIENTS:</span> Shea Butter, Beef Tallow, Beeswax, Grape Seed Oil, Vegetable Glycerin, Lanolin, Panthenol, Gluconolactone, Sodium Benzoate, Allantoin, Manuka Honey, Vitamin E, Tea Tree Essential Oil, Lemon Myrtle Essential Oil, Rosemary Oleoresin Extract.</p>
    <p class="tagline"><strong>Getting you back</strong>On your feet</p>
    <p class="social-handle"><span class="social-dot"></span>@bramblekeepnz</p>

    <div class="front">
      <div class="fern-area dark" role="img" aria-label="Dark fern fronds framing the front panel"></div>
      <div class="brand">
        <span class="brand-mark"></span>
        <p class="brand-name">Bramble Keep NZ</p>
      </div>
      <h1 class="product-name">Ridge Mender<br>Balm</h1>
      <p class="product-tagline">For Hardworking Soles</p>
      <p class="net-contents">120ml</p>
      <div class="origin-badge"><b>MADE IN</b><small>NEW ZEALAND</small></div>
    </div>

    <div class="directions">
      <h2 class="directions-title">DIRECTIONS:</h2>
      <svg class="step-icon" style="top:18px" viewBox="0 0 36 36" aria-hidden="true">
        <path d="M3 14h24v14c0 3-5 5-12 5S3 31 3 28z" fill="#8a5a2b"/>
        <ellipse cx="15" cy="14" rx="12" ry="4" fill="#f4efe6" stroke="#5a4a3e" stroke-width="1.5"/>
        <circle cx="28" cy="27" r="7" fill="#f4efe6" stroke="#5a4a3e" stroke-width="1.5"/>
        <path d="M28 22c2 3 3 4 3 6a3 3 0 0 1-6 0c0-2 1-3 3-6z" fill="#8a5a2b"/>
      </svg>
      <p class="step-text" style="top:27px">Apply generously.</p>

      <div class="step-icon icon-placeholder foot" style="top:56px" role="img" aria-label="Foot icon"></div>
      <p class="step-text" style="top:62px">To clean, dry feet, focusing on heels and thick or cracked areas.</p>

      <div class="step-icon icon-placeholder sock" style="top:99px" role="img" aria-label="Sock with moon icon"></div>
      <p class="step-text" style="top:105px">For cracked heels, wear our moisture-locking socks overnight.</p>

      <svg class="step-icon" style="top:146px" viewBox="0 0 36 36" aria-hidden="true">
        <rect x="3" y="5" width="24" height="22" rx="2" fill="none" stroke="#5a4a3e" stroke-width="2"/>
        <rect x="3" y="5" width="24" height="6" fill="#8a5a2b"/>
        <g fill="#5a4a3e"><rect x="7" y="14" width="3" height="3"/><rect x="12" y="14" width="3" height="3"/><rect x="17" y="14" width="3" height="3"/><rect x="7" y="20" width="3" height="3"/><rect x="12" y="20" width="3" height="3"/></g>
        <circle cx="26" cy="27" r="7" fill="#8a5a2b"/>
        <path d="M22.5 27l2.5 2.5 4.5-5" stroke="#f4efe6" stroke-width="2" fill="none"/>
      </svg>
      <p class="step-text" style="top:155px">Use daily.</p>

      <svg class="pao-icon" viewBox="0 0 30 32" aria-hidden="true">
        <path d="M4 5l20-5 1 3-20 6z" fill="#1f3a2b"/>
        <ellipse cx="15" cy="14" rx="13" ry="3.5" fill="#1f3a2b"/>
        <path d="M2 14h26v14c0 2-6 3-13 3S2 30 2 28z" fill="#1f3a2b"/>
        <text x="15" y="27" text-anchor="middle" font-family="Inter, sans-serif" font-size="8" font-weight="700" fill="#f4efe6">6M</text>
      </svg>
    </div>
  </div>
</section>

<section class="label" style="top:283px;">
  <div class="label-inner">
    <p class="storage"><span class="field-title">STORAGE:</span> Keep out of direct sunlight. Best used within six months of opening.</p>
    <div class="divider"></div>
    <p class="ingredients"><span class="field-title">INGREDIENTS:</span> Shea Butter, Beef Tallow, Beeswax, Grape Seed Oil, Vegetable Glycerin, Lanolin, Panthenol, Gluconolactone, Sodium Benzoate, Allantoin, Manuka Honey, Vitamin E, Tea Tree Essential Oil, Lemon Myrtle Essential Oil, Rosemary Oleoresin Extract.</p>
    <p class="tagline"><strong>Getting you back</strong>On your feet</p>
    <p class="social-handle"><span class="social-dot"></span>@bramblekeepnz</p>

    <div class="front">
      <div class="fern-area light" role="img" aria-label="Soft blue-grey fern fronds framing the front panel"></div>
      <div class="brand">
        <span class="brand-mark"></span>
        <p class="brand-name">Bramble Keep NZ</p>
      </div>
      <h1 class="product-name">Ridge Mender<br>Balm</h1>
      <p class="product-tagline">For Hardworking Soles</p>
      <p class="net-contents">120ml</p>
      <div class="origin-badge"><b>MADE IN</b><small>NEW ZEALAND</small></div>
    </div>

    <div class="directions">
      <h2 class="directions-title">DIRECTIONS:</h2>
      <svg class="step-icon" style="top:18px" viewBox="0 0 36 36" aria-hidden="true">
        <path d="M3 14h24v14c0 3-5 5-12 5S3 31 3 28z" fill="#8a5a2b"/>
        <ellipse cx="15" cy="14" rx="12" ry="4" fill="#f4efe6" stroke="#5a4a3e" stroke-width="1.5"/>
        <circle cx="28" cy="27" r="7" fill="#f4efe6" stroke="#5a4a3e" stroke-width="1.5"/>
        <path d="M28 22c2 3 3 4 3 6a3 3 0 0 1-6 0c0-2 1-3 3-6z" fill="#8a5a2b"/>
      </svg>
      <p class="step-text" style="top:27px">Apply generously.</p>

      <div class="step-icon icon-placeholder foot" style="top:56px" role="img" aria-label="Foot icon"></div>
      <p class="step-text" style="top:62px">To clean, dry feet, focusing on heels and thick or cracked areas.</p>

      <div class="step-icon icon-placeholder sock" style="top:99px" role="img" aria-label="Sock with moon icon"></div>
      <p class="step-text" style="top:105px">For cracked heels, wear our moisture-locking socks overnight.</p>

      <svg class="step-icon" style="top:146px" viewBox="0 0 36 36" aria-hidden="true">
        <rect x="3" y="5" width="24" height="22" rx="2" fill="none" stroke="#5a4a3e" stroke-width="2"/>
        <rect x="3" y="5" width="24" height="6" fill="#8a5a2b"/>
        <g fill="#5a4a3e"><rect x="7" y="14" width="3" height="3"/><rect x="12" y="14" width="3" height="3"/><rect x="17" y="14" width="3" height="3"/><rect x="7" y="20" width="3" height="3"/><rect x="12" y="20" width="3" height="3"/></g>
        <circle cx="26" cy="27" r="7" fill="#8a5a2b"/>
        <path d="M22.5 27l2.5 2.5 4.5-5" stroke="#f4efe6" stroke-width="2" fill="none"/>
      </svg>
      <p class="step-text" style="top:155px">Use daily.</p>

      <svg class="pao-icon" viewBox="0 0 30 32" aria-hidden="true">
        <path d="M4 5l20-5 1 3-20 6z" fill="#1f3a2b"/>
        <ellipse cx="15" cy="14" rx="13" ry="3.5" fill="#1f3a2b"/>
        <path d="M2 14h26v14c0 2-6 3-13 3S2 30 2 28z" fill="#1f3a2b"/>
        <text x="15" y="27" text-anchor="middle" font-family="Inter, sans-serif" font-size="8" font-weight="700" fill="#f4efe6">6M</text>
      </svg>
    </div>
  </div>
</section>

</body>
</html>
```